RK Tannery Construction Inc.

Design a new business card for our construction company
To be removed from current card:
Delete 25 years
Delete Tenant fit up Renovations section

```html
<!DOCTYPE html>
<html lang="en">
<head>
<meta charset="utf-8">
<title>RK Tannery Construction Inc. – Business Card</title>
<link rel="stylesheet" href="https://fonts.googleapis.com/css2?family=Montserrat:wght@400;500;600;700&display=swap">
<style>
  :root {
    --backdrop: #e6dfd6;
    --card: #f4f1ed;
    --card-edge: #ddd6cd;
    --purple: #4f2a6a;
    --green: #1d6a4c;
    --ink: #2c2a2a;
  }
  * { box-sizing: border-box; margin: 0; padding: 0; }
  html, body {
    width: 1200px;
    height: 1047px;
    overflow: hidden;
    background: var(--backdrop);
    font-family: "Montserrat", Arial, sans-serif;
  }
  .card {
    position: absolute;
    left: 150px;
    top: 288px;
    width: 940px;
    height: 520px;
    background: var(--card);
    border: 1px solid var(--card-edge);
    border-radius: 26px;
    box-shadow: 0 6px 24px rgba(60, 45, 30, 0.12);
  }
  .brand {
    position: absolute;
    left: 68px;
    top: 40px;
    width: 810px;
    color: var(--purple);
    font-weight: 600;
    text-transform: uppercase;
  }
  .brand-name {
    display: block;
    font-size: 98px;
    line-height: 1;
    letter-spacing: 1px;
  }
  .brand-sub {
    display: block;
    margin-top: 4px;
    font-size: 44px;
    letter-spacing: 6.4px;
    line-height: 1.1;
  }
  .person {
    position: absolute;
    left: 38px;
    right: 38px;
    top: 292px;
    display: flex;
    align-items: center;
    gap: 14px;
  }
  .person .rule {
    flex: 1;
    height: 2px;
    background: var(--green);
  }
  .person-name {
    font-size: 31px;
    font-weight: 700;
    letter-spacing: 0.5px;
    text-transform: uppercase;
  }
  .person-name .first { color: var(--purple); }
  .person-name .last { color: var(--green); }
  .contacts {
    position: absolute;
    left: 40px;
    top: 350px;
    list-style: none;
    color: var(--ink);
    font-size: 22px;
    font-weight: 500;
  }
  .contacts li {
    display: flex;
    align-items: center;
    height: 34px;
  }
  .contacts svg {
    width: 20px;
    height: 20px;
    margin-right: 10px;
    fill: var(--green);
  }
  .address {
    position: absolute;
    right: 36px;
    top: 418px;
    text-align: right;
    font-style: normal;
    color: var(--ink);
    font-size: 22px;
    font-weight: 500;
    line-height: 34px;
  }
</style>
</head>
<body>
  <div class="card">
    <h1 class="brand">
      <span class="brand-name">RK Tannery</span>
      <span class="brand-sub">Construction Inc.</span>
    </h1>

    <div class="person">
      <span class="rule"></span>
      <span class="person-name"><span class="first">Martin</span> <span class="last">Tannery</span></span>
      <span class="rule"></span>
    </div>

    <ul class="contacts">
      <li>
        <svg viewBox="0 0 24 24" aria-hidden="true"><path d="M3 9c0-3 4-5 9-5s9 2 9 5v2h-5V9H8v2H3zM6 12h12l2 8H4z"/></svg>
        613-555-0142 ext: 221
      </li>
      <li>
        <svg viewBox="0 0 24 24" aria-hidden="true"><path d="M7 2h10a1.5 1.5 0 0 1 1.5 1.5v17A1.5 1.5 0 0 1 17 22H7a1.5 1.5 0 0 1-1.5-1.5v-17A1.5 1.5 0 0 1 7 2zm0.5 3v13h9V5zm4.5 14.2a1 1 0 1 0 0 .01z"/></svg>
        613-555-0187
      </li>
      <li>
        <svg viewBox="0 0 24 24" aria-hidden="true"><path d="M2 6h20v1.5l-10 6-10-6zM2 9.8l10 6 10-6V19H2z"/></svg>
        martin@rktanneryconst.ca
      </li>
      <li>
        <svg viewBox="0 0 24 24" aria-hidden="true"><path d="M12 2a10 10 0 1 0 0 20 10 10 0 0 0 0-20zm0 2c1.3 1.5 2.2 3.7 2.5 7h-5C9.8 7.7 10.7 5.5 12 4zm-2.6.5C8.6 6.2 8 8.4 7.8 11H4.1a8 8 0 0 1 5.3-6.5zm5.2 0A8 8 0 0 1 19.9 11h-3.7c-.2-2.6-.8-4.8-1.6-6.5zM4.1 13h3.7c.2 2.6.8 4.8 1.6 6.5A8 8 0 0 1 4.1 13zm5.4 0h5c-.3 3.3-1.2 5.5-2.5 7-1.3-1.5-2.2-3.7-2.5-7zm6.7 0h3.7a8 8 0 0 1-5.3 6.5c.8-1.7 1.4-3.9 1.6-6.5z"/></svg>
        www.rktanneryconstruction.ca
      </li>
    </ul>

    <address class="address">
      2180 Halden Rd., Suite 100,<br>
      Ottawa, ON K1B 4T7
    </address>
  </div>
</body>
</html>
```